Designing a website that functions as the shop window for the various aspects of my business -...

I need a website, with separate webpages covering the different components of my practice (small animal consultancy, equine behaviour consultancy, legal case work and education provider). I have a website (www.petmindstudio-example.ie) but I haven't updated it in recent years to reflect the newer developments / aspects of my business. Most of my work has been in Ireland but I would like to begin to create an international profile, particularly with regard to the legal casework and offering education within the international horse industry. My overall goal is to improve understanding of animals and animal behaviour, and by doing so, help to reduce the performance of behaviour problems, and also improve animal welfare as a result.

Target Market(s)

Horse and dog owners, horse riders, veterinary surgeons, solicitors

Industry/Entity Type

Legal

Logo Text

Text to be decided on

Number of Pages Required

5+ page

Font styles to use
Sans Serif
Decorative
Script

Colors

Designer to choose colors to be used in the design.

Requirements
Must have
• Relevant content from the attached Flyer including photos
• Use of the phrases:
• 'Understanding Animals'
• Improving animals lives through better understanding
• Science-based, up-to-date relevant information regarding animal behaviour
Nice to have
• 'Leading professional service educating people in understanding animals'
• Separate pages for 1) About, 2) Canine and Feline behaviour Consultancy 3) Equine Consultancy 4) Legal expert witness Consultancy 5) Education 6, FAQs
Should not have
• Prices of services (as these may change from time to time)

```html
<!DOCTYPE html>
<html lang="en">
<head>
<meta charset="utf-8">
<title>Pet Mind Studio – Understanding Animals</title>
<link href="https://fonts.googleapis.com/css2?family=Roboto:wght@400;500;700;900&display=swap" rel="stylesheet">
<style>
:root{
  --green:#6a9e48;
  --crimson:#b23a52;
  --ink:#4a4a4a;
  --text:#3c3c3c;
  --light:#f7f7f7;
  --footer:#454545;
  --footer-bar:#303030;
  --white:#ffffff;
}
*{margin:0;padding:0;box-sizing:border-box}
html,body{width:1200px;height:2625px;overflow:hidden;background:var(--white)}
body{position:relative;font-family:'Roboto',Arial,sans-serif;color:var(--text)}
.abs{position:absolute}
.photo{position:absolute}

/* header */
.site-header{left:0;top:0;width:1200px;height:109px;background:var(--white)}
.brand{display:flex;align-items:center;gap:14px}
.brand-dot{width:56px;height:56px;border-radius:50%;background:var(--crimson)}
.brand-name{font-weight:500;font-size:26px;color:#7a7a7a}
.nav{display:flex;gap:24px;font-size:11.5px;font-weight:700;color:#333;text-transform:uppercase;letter-spacing:.1px}

/* hero */
.hero{left:0;top:109px;width:1200px;height:610px}
.hero-photo{left:0;top:0;width:1200px;height:610px;
  background:linear-gradient(90deg,#6a6644 0%,#8f8a58 35%,#b8ad74 60%,#cdc28c 100%)}
.hero-title{left:709px;top:256px;width:370px;text-align:center;color:var(--white);font-weight:700;font-size:47px;line-height:1}
.hero-title-big{left:709px;top:304px;width:370px;text-align:center;color:var(--green);font-weight:700;font-size:80px;line-height:1}
.hero-btn{left:710px;top:401px;width:368px;height:67px;background:var(--crimson);color:var(--white);
  font-weight:700;font-size:32px;display:flex;align-items:center;justify-content:center}

/* intro */
.intro{left:0;top:719px;width:1200px;height:430px;background:var(--light)}
.intro h1{position:absolute;left:95px;top:58px;font-size:50px;font-weight:700;color:var(--ink);letter-spacing:.3px}
.intro p{position:absolute;left:95px;top:150px;width:662px;font-size:19px;font-weight:700;line-height:27px;letter-spacing:.35px;color:var(--text)}
.intro-photo{left:802px;top:53px;width:282px;height:314px;background:linear-gradient(135deg,#3a2a22,#7a5440 50%,#b08a70)}
.btn{position:absolute;background:var(--green);color:var(--white);font-weight:700;display:flex;align-items:center;justify-content:center;text-transform:uppercase}
.intro .btn{left:535px;top:347px;width:123px;height:36px;font-size:17px}

/* offer */
.offer{left:0;top:1149px;width:1200px;height:641px;
  background:radial-gradient(ellipse at 20% 40%,#dedede,#eeeeee 60%,#f1f1f1)}
.section-title{position:absolute;left:0;width:1200px;text-align:center;font-size:38px;font-weight:700;color:var(--ink)}
.offer .section-title{top:40px}
.card{position:absolute;top:128px;width:256px;height:500px}
.card-photo{height:183px;width:100%}
.card h3{margin-top:62px;font-size:17px;font-weight:700;text-align:center;color:#333;line-height:22px;text-transform:uppercase}
.card .sub{font-size:10px;font-weight:700;text-align:center;margin-top:2px;color:#444}
.card p{margin-top:10px;font-size:9.6px;font-weight:700;line-height:12.6px;color:#555}
.card .btn{width:102px;height:33px;font-size:15px;top:421px}

/* science */
.science{left:0;top:1790px;width:1200px;height:455px;background:var(--light)}
.science .section-title{top:28px}
.video-photo{left:125px;top:105px;width:447px;height:350px;background:linear-gradient(180deg,#6e9a3a,#a8c060 55%,#c7cf6a)}
.news-photo{left:647px;top:105px;width:460px;height:350px;background:linear-gradient(180deg,#4a4e52,#6b7074 45%,#3a3430)}

/* latest */
.latest{left:0;top:2245px;width:1200px;height:220px;background:var(--white)}
.latest h2{position:absolute;font-size:26px;font-weight:700;color:var(--ink);text-align:center}
.latest p{position:absolute;font-size:11.5px;font-weight:700;line-height:15.5px;color:#444}

/* footer */
.site-footer{left:0;top:2465px;width:1200px;height:110px;background:var(--footer)}
.site-footer .brand-name{color:#dcdcdc}
.site-footer .nav{color:#e6e6e6;font-size:11px;font-weight:500}
.footer-bar{left:0;top:2575px;width:1200px;height:50px;background:var(--footer-bar);color:var(--white)}
.copyright{left:104px;top:17px;font-size:13px;font-weight:700}
.social{right:83px;top:12px;display:flex;gap:10px}
.social span{width:26px;height:26px;border-radius:3px;background:var(--white)}
</style>
</head>
<body>

<header class="abs site-header">
  <div class="abs brand" style="left:86px;top:26px">
    <span class="brand-dot"></span>
    <span class="brand-name">Pet Mind Studio</span>
  </div>
  <nav class="abs nav" style="left:460px;top:48px">
    <span>About us</span><span>Canine &amp; Feline Behaviour Consultancy</span><span>Equine Consultancy</span><span>Legal Expert</span><span>Education</span>
  </nav>
</header>

<section class="abs hero">
  <div class="photo hero-photo" role="img" aria-label="Spaniel puppy carrying an orange ball across a sunny field"></div>
  <div class="abs hero-title">UNDERSTANDING</div>
  <div class="abs hero-title-big">ANIMALS</div>
  <div class="abs hero-btn">CONSULTANCY</div>
</section>

<section class="abs intro">
  <h1>IMPROVING ANIMALS LIVES</h1>
  <p>Animals have been used by humans for a variety of purposes, including as a source of food, for hunting, for mobility, to help win battles, for sport - and most recently, for companionship. Whether we are dog or cat lovers, horseriders or owners, through the course of our relationship with our animals, many of us will be faced with problem behaviours, such as aggression, excessive barking, destructiveness (dogs), spraying, fear problems, aggression (cats), bucking, refusing to load into trailers, rearing, shying (horses).</p>
  <div class="photo intro-photo" role="img" aria-label="Woman resting her head against a brown horse"></div>
  <div class="btn">More</div>
</section>

<section class="abs offer">
  <h2 class="section-title">WHAT WE OFFER</h2>

  <div class="card" style="left:60px">
    <div class="card-photo" role="img" aria-label="Close-up of a horse's eye beside a person's eye" style="background:linear-gradient(90deg,#4a2c1c,#8a5a3a 48%,#c9a890 52%,#e0c4b0)"></div>
    <h3>Behaviour consultations</h3>
    <p>During a behaviour consultation, an individual assessment of the horse is carried out, incorporating information regarding the horses health, management, past training and competition history, current training methods and outcomes, behaviour patterns displayed, problem behaviours or simply poor performance.</p>
    <div class="btn" style="left:80px">Find more</div>
  </div>

  <div class="card" style="left:342px">
    <div class="card-photo" role="img" aria-label="Young woman with a dark horse in green woodland" style="background:linear-gradient(135deg,#2e4a1e,#5a7a34 50%,#a07050)"></div>
    <h3>Training sessions</h3>
    <p>Individual training sessions with horse and rider, designed to address training problems, the performance of problem behaviours or general poor performance. Each training session will focus on equipping the rider with a good understanding of learning theory, and how to apply it to achieve optimal results with their horse.</p>
    <div class="btn" style="left:80px">Find more</div>
  </div>

  <div class="card" style="left:621px">
    <div class="card-photo" role="img" aria-label="Rider jumping a horse over a fence with mountains behind" style="background:linear-gradient(180deg,#8fb4d8,#b8cfe0 45%,#7a9a5a 70%,#5a7a40)"></div>
    <h3>Training your horse</h3>
    <div class="sub">- THEORY AND PRACTICE</div>
    <p style="margin-top:8px">This course incorporates both classroom sessions and practical sessions in the arena, developing the rider skills in training, both in hand and under saddle. The course will be run for groups of four or more, allowing riders, or participants without a horse, but interested in learning, to work in a safe environment.</p>
    <div class="btn" style="left:78px">Find more</div>
  </div>

  <div class="card" style="left:889px">
    <div class="card-photo" role="img" aria-label="Rider on a horse in a golden field at dusk" style="background:linear-gradient(180deg,#8a96a8,#b8a890 45%,#a88050 70%,#7a5a30)"></div>
    <h3>Training, performance<br>and welfare</h3>
    <p>During this course, run for groups of 8 to 12, students will greatly deepen their understanding of the horse, through attending lectures, workshops, demonstrations and individual training sessions. The course will address a range of areas including training methods, welfare, the horses physiology, neurology, effects of management and diet on performance.</p>
    <div class="btn" style="left:82px">Find more</div>
  </div>
</section>

<section class="abs science">
  <h2 class="section-title">SCIENCE-BASED INFORMATION</h2>
  <div class="photo video-photo" role="img" aria-label="Labrador puppy sitting in grass with yellow flowers"></div>
  <svg class="abs" style="left:283px;top:215px" width="100" height="100" viewBox="0 0 100 100" aria-hidden="true">
    <circle cx="50" cy="50" r="44" fill="rgba(255,255,255,0.15)" stroke="#6a9e48" stroke-width="6"/>
    <path d="M38 28 L74 50 L38 72 Z" fill="#6a9e48"/>
  </svg>
  <div class="photo news-photo" role="img" aria-label="Lecture room with audience watching a projected presentation"></div>
</section>

<section class="abs latest">
  <h2 style="left:125px;top:20px;width:447px">LATEST VIDEO</h2>
  <p style="left:114px;top:88px;width:458px">So why do problems arise? In investigating and treating behaviour problems, many factors need to be taken into account, including the animal's breeding (what genetic makeup the animal has inherited from it's parents), health, previous experience, normal behaviour patterns of that species (dogs will display very different normal behaviours to cats, or to horses) and motivational factors</p>
  <h2 style="left:647px;top:20px;width:460px">LATEST NEWS</h2>
  <p style="left:647px;top:88px;width:466px">Treatment of behaviour problems using scientific knowledge about all of the above factors is a relatively recent development, spanning only the last 60 years approximately, but in that time, major advances have been made, and continue to be made, in our understanding of what causes behaviour problems to develop - and equally importantly - how these problems can be treated.</p>
</section>

<footer class="abs site-footer">
  <div class="abs brand" style="left:110px;top:27px">
    <span class="brand-dot"></span>
    <span class="brand-name">Pet Mind Studio</span>
  </div>
  <nav class="abs nav" style="left:502px;top:48px">
    <span>About us</span><span>Canine &amp; Feline Behaviour Consultancy</span><span>Equine Consultancy</span><span>Legal Expert</span><span>Education</span>
  </nav>
</footer>

<div class="abs footer-bar">
  <div class="abs copyright">Copyright Pet Mind Studio</div>
  <div class="abs social" aria-label="Social links"><span></span><span></span><span></span></div>
</div>

</body>
</html>
```